Nutrition business needs logo & business card design

We need a business card & logo design for a new company based in Toronto, Ontario Canada called Verdel Wellcraft.

We provide nutrition service using metrics as guide to manage client's progress. Our service creates individualized nutrition and lifestyle strategies that focuses on improving Performance, Longevity and Weight Loss. I would like to see designs that use the color of green, gray, blue and white.

The final design should:

--convey a feeling of connectedness with positive transformation.

-- communicate the idea of awareness with guided effort that yields personal independence for a better and more productive life

Target Market(s)

Professionals who work in the IT/Computer/Engineering/Banking industry specifically Directors, Managers, CEO's.

Industry/Entity Type

Health And Wellness

Contact Information for Business Card

Domric Hale, Owner
email: DHALE@verdelwellcraft.example
tel: - 555-274-9038

Logo Text

better health through analytics or measure to manage

Font styles to use
Other font styles liked:
• Garamound

Colors
ffffff
abd037
85acd3
757575
34a7d7

Requirements
Must have
• Good contrast and decent size font - ease of readability, aesthetically nice colors
Nice to have
• image of chart or graph that conveys measurement or analytics
Should not have
• Borders, images of food,

```html
<!DOCTYPE html>
<html lang="en">
<head>
<meta charset="utf-8">
<title>Verdel Wellcraft — Business Card</title>
<link rel="stylesheet" href="https://fonts.googleapis.com/css2?family=Josefin+Sans:wght@300;400&family=Montserrat:wght@400;700&family=Cormorant+Garamond:ital,wght@1,500&display=swap">
<style>
  :root {
    --backdrop: #e4e1dc;
    --charcoal: #2e2f31;
    --lime: #a6cf38;
    --white: #ffffff;
    --grid-line: #e6e9ec;
    --ink: #2a2a2a;
    --ink-soft: #4a4a4a;
    --chart-line: #d4d8dc;
  }
  * { margin: 0; padding: 0; box-sizing: border-box; }
  html, body {
    width: 1200px;
    height: 1023px;
    overflow: hidden;
    background: var(--backdrop);
  }
  .stage {
    width: 1200px;
    height: 1023px;
    display: flex;
    align-items: center;
    justify-content: center;
  }
  .card {
    position: relative;
    width: 900px;
    height: 514px;
    background: var(--white);
    box-shadow: 0 14px 34px rgba(0,0,0,0.22);
    overflow: hidden;
  }
  .card__brand-panel {
    position: absolute;
    left: 0; top: 0;
    width: 100%;
    height: 262px;
    background: var(--charcoal);
    display: flex;
    align-items: center;
    padding-left: 120px;
  }
  .brand-name {
    font-family: "Josefin Sans", sans-serif;
    font-weight: 300;
    font-size: 40px;
    letter-spacing: 14px;
    color: var(--white);
    text-transform: uppercase;
    padding-top: 6px;
    white-space: nowrap;
  }
  .card__tagline-band {
    position: absolute;
    left: 0; top: 274px;
    width: 100%;
    height: 56px;
    background: var(--lime);
    display: flex;
    align-items: center;
    padding-left: 120px;
  }
  .tagline {
    font-family: "Cormorant Garamond", serif;
    font-style: italic;
    font-weight: 500;
    font-size: 26px;
    color: var(--white);
    letter-spacing: 0.5px;
  }
  .card__contact-panel {
    position: absolute;
    left: 0; top: 340px;
    width: 100%;
    height: 174px;
    background-color: var(--white);
    background-image:
      linear-gradient(var(--grid-line) 1px, transparent 1px),
      linear-gradient(90deg, var(--grid-line) 1px, transparent 1px);
    background-size: 22px 22px;
  }
  .trend-chart {
    position: absolute;
    left: 0; top: 0;
    width: 100%;
    height: 100%;
  }
  .holder {
    position: absolute;
    left: 120px;
    top: 40px;
  }
  .holder__name {
    font-family: "Montserrat", sans-serif;
    font-weight: 700;
    font-size: 40px;
    letter-spacing: -1px;
    color: var(--ink);
    line-height: 1;
  }
  .holder__role {
    font-family: "Montserrat", sans-serif;
    font-weight: 400;
    font-size: 24px;
    color: var(--ink-soft);
    margin-top: 12px;
    line-height: 1.1;
  }
  .contact-lines {
    position: absolute;
    left: 480px;
    top: 40px;
    font-family: "Montserrat", sans-serif;
    font-weight: 400;
    font-size: 22px;
    color: var(--ink-soft);
    line-height: 1.7;
  }
</style>
</head>
<body>
  <main class="stage">
    <article class="card">
      <header class="card__brand-panel">
        <h1 class="brand-name">Verdel Wellcraft</h1>
      </header>
      <div class="card__tagline-band">
        <p class="tagline">Measure to Manage, Living Well</p>
      </div>
      <section class="card__contact-panel">
        <svg class="trend-chart" viewBox="0 0 900 174" preserveAspectRatio="none" aria-hidden="true">
          <polyline points="40,168 200,150 330,162 470,146 600,156 740,138 880,148"
                    fill="none" stroke="var(--chart-line)" stroke-width="2"/>
        </svg>
        <div class="holder">
          <p class="holder__name">Domric Hale</p>
          <p class="holder__role">Owner</p>
        </div>
        <div class="contact-lines">
          <p class="contact-lines__email">DHALE@verdelwellcraft.example</p>
          <p class="contact-lines__phone">555-274-9038</p>
        </div>
      </section>
    </article>
  </main>
</body>
</html>
```